Stationery Design Project

I would like professional stationery that will be branded with our logo.

also, I have application- multipage that I would like to brand. I will attach an example of one of the pages.

Perhaps- this could be the same design, but due to spacing, it may be best to do slight variations.

Target Market(s)

The audience is our donors and supporters who have a heart for the disenfranchised. They are mostly professional and often have significant wealth. They do their work with excellence and I want an image that makes them feel confident we know what we are doing. this is why i tend to say i want a professional look. Also, I want the feel to be uplifting, something that is somewhat artistic and classy.

Industry/Entity Type

It Professional

Font styles to use
Serif

Requirements
Must have
• Generally, simple but I do want a stylized look...

583-274-6150
www.brightfernway.org
PO Box 384729 Fernvale, TX 75904
admin@brightfernway.org
Nice to have
• i like to use the colors in our logo
Should not have
• hearts and country look

```html
<!DOCTYPE html>
<html lang="en">
<head>
<meta charset="utf-8">
<title>Bright Fern Way – Letterhead</title>
<link rel="stylesheet" href="https://fonts.googleapis.com/css2?family=Tinos:ital,wght@0,400;1,400&display=swap">
<style>
  :root {
    --ink: #111111;
    --brand-blue: #0b4f97;
    --sky-blue: #3ea4dc;
    --sun-yellow: #f5c400;
    --paper: #ffffff;
  }
  html, body {
    margin: 0;
    padding: 0;
    overflow: hidden;
    background: var(--paper);
  }
  .letterhead {
    position: relative;
    width: 848px;
    height: 1200px;
    overflow: hidden;
    background: var(--paper);
    font-family: "Tinos", "Times New Roman", serif;
    color: var(--ink);
  }
  .brand {
    position: absolute;
    left: 28px;
    top: 20px;
    display: flex;
    align-items: center;
  }
  .brand-dot {
    width: 104px;
    height: 104px;
    border-radius: 50%;
    background: var(--brand-blue);
    flex: none;
  }
  .brand-name {
    margin: 0 0 0 14px;
    font-size: 33px;
    font-weight: 400;
    letter-spacing: 1px;
    text-transform: uppercase;
    color: var(--ink);
    line-height: 1;
  }
  .tagline {
    position: absolute;
    left: 262px;
    top: 96px;
    margin: 0;
    font-style: italic;
    font-size: 17px;
    color: var(--ink);
  }
  .contact {
    position: absolute;
    left: 563px;
    top: 37px;
    margin: 0;
    padding: 0;
    list-style: none;
    font-size: 17px;
    line-height: 22.7px;
  }
  .contact li {
    display: flex;
    align-items: center;
    gap: 5px;
    white-space: nowrap;
  }
  .contact-icon {
    width: 14px;
    height: 14px;
    flex: none;
    fill: var(--sun-yellow);
  }
  .footer-band {
    position: absolute;
    left: 0;
    top: 0;
    width: 848px;
    height: 1200px;
    pointer-events: none;
  }
  .band-deep { fill: var(--brand-blue); }
  .line-sky { fill: none; stroke: var(--sky-blue); stroke-width: 6; }
  .line-sun { fill: none; stroke: var(--sun-yellow); stroke-width: 4; }
</style>
</head>
<body>
<main class="letterhead">
  <svg class="footer-band" viewBox="0 0 848 1200" aria-hidden="true">
    <path class="line-sun" d="M120,1108 C330,1150 560,1150 760,1100"/>
    <path class="line-sky" d="M0,1098 C300,1158 560,1158 848,1098"/>
    <path class="band-deep" d="M0,1110 C300,1170 560,1170 848,1110 L848,1200 L0,1200 Z"/>
  </svg>

  <header class="brand">
    <span class="brand-dot" aria-hidden="true"></span>
    <h1 class="brand-name">Bright Fern Way</h1>
  </header>
  <p class="tagline">Where bright paths open</p>

  <ul class="contact">
    <li>
      <svg class="contact-icon" viewBox="0 0 16 16" aria-hidden="true"><path d="M3.6 1.5l2.2 2.6-1.3 1.6c.9 2 2.6 3.7 4.6 4.6l1.6-1.3 2.6 2.2-1.4 2.3C6.6 15 1 9.4 1.5 3z"/></svg>
      <span>583-274-6150</span>
    </li>
    <li>
      <svg class="contact-icon" viewBox="0 0 16 16" aria-hidden="true"><path d="M8 1a7 7 0 100 14A7 7 0 008 1zm0 1.6c.8.8 1.4 2.3 1.6 4.6H6.4C6.6 4.9 7.2 3.4 8 2.6zM2.7 8.8h2.2c.1 1.7.5 3.1 1 4.2a5.5 5.5 0 01-3.2-4.2zm0-1.6A5.5 5.5 0 015.9 3c-.5 1.1-.9 2.5-1 4.2zm5.3 6.2c-.8-.8-1.4-2.3-1.6-4.6h3.2c-.2 2.3-.8 3.8-1.6 4.6zm2.1-.4c.5-1.1.9-2.5 1-4.2h2.200a5.5 5.5 0 01-3.2 4.2zm1-5.8c-.1-1.7-.5-3.1-1-4.2a5.5 5.5 0 013.2 4.2z"/></svg>
      <span>www.brightfernway.org</span>
    </li>
    <li>
      <svg class="contact-icon" viewBox="0 0 16 16" aria-hidden="true"><path d="M1 4h14v9H1zM2.5 5.3v.4L8 9.3l5.5-3.6v-.4z"/></svg>
      <span>admin@brightfernway.org</span>
    </li>
    <li>
      <svg class="contact-icon" viewBox="0 0 16 16" aria-hidden="true"><path d="M8 1.5L.8 8h2.2v6.5h3.8v-4h2.4v4h3.8V8h2.2z"/></svg>
      <span>PO Box 384729 Fernvale, TX 75904</span>
    </li>
  </ul>
</main>
</body>
</html>
```